Marlowe Oakhaven Builders LLC

Roofing, windows, gutters services offered.
0% 6 months interest free financing
Quorvin windows
Tillbrook windows
RUV roofing shingles
PEM roofing shingles
Offering 30-50 year warranties.
Accepting all major credit cards, checks
Emergency services available
Updates

Went on vacation/holiday

Target Market(s)

Roofing contractors

Industry/Entity Type

Roofing

Number of Pages Required

3 page

Font styles to use
Sans Serif

Requirements
Must have
• MUST HAVE SEO all necessary codes!!!!!!!!!!
• also I want button for "schedule appointment" so I can receive notification of an appointment, and also need live calendar integrated in that button
Nice to have
• Modern, professional site

```html
<!DOCTYPE html>
<html lang="en">
<head>
<meta charset="utf-8">
<title>Marlowe Oakhaven Builders LLC | Roofing, Windows &amp; Gutters</title>
<meta name="description" content="Marlowe Oakhaven Builders LLC – roofing, windows and gutters services and repair. 0% interest financing, 30-50 year warranties, emergency services.">
<meta name="viewport" content="width=1200">
<link rel="stylesheet" href="https://fonts.googleapis.com/css2?family=Lato:wght@400;700;900&display=swap">
<style>
:root{
  --green:#078a3d;
  --green-dark:#056e30;
  --blue:#27a6df;
  --navy:#0f2552;
  --text:#555c66;
  --light:#f2f4f5;
  --dark:#0e1626;
  --white:#ffffff;
}
*{box-sizing:border-box;margin:0;padding:0}
html,body{width:1200px;height:3390px;overflow:hidden}
body{font-family:"Lato",Arial,sans-serif;color:var(--text);background:var(--white);position:relative;font-size:13px;line-height:1.6}
.abs{position:absolute}
p{font-size:12.5px;line-height:1.75}
.photo{position:absolute}

/* header */
.site-header{position:absolute;left:0;top:0;width:1200px;height:118px}
.brand{left:160px;top:22px;display:flex;align-items:center;gap:10px}
.brand-dot{width:34px;height:34px;border-radius:50%;background:var(--blue)}
.brand-name{width:140px;color:var(--green);font-weight:700;font-size:11.5px;line-height:1.3;text-transform:uppercase}
.social{left:618px;top:22px;display:flex;gap:12px}
.social span{width:26px;height:26px;border-radius:50%;background:var(--navy);display:block}
.call{left:814px;top:14px;color:var(--navy)}
.call small{display:block;font-size:12.5px;font-weight:700;letter-spacing:.2px}
.call strong{display:block;font-size:29px;font-weight:900;line-height:1.1}
.main-nav{left:393px;top:90px;width:807px;height:28px;background:var(--green);display:flex;padding-left:10px}
.main-nav a{color:var(--white);text-decoration:none;font-size:11px;font-weight:700;text-transform:uppercase;padding:0 11px;line-height:28px}
.main-nav a.active{background:var(--green-dark)}

/* hero */
.hero{left:0;top:118px;width:1200px;height:452px;background:linear-gradient(180deg,#8fb7d8 0%,#c7d6e2 35%,#b4a497 70%,#8b6f60 100%)}
.hero-card{left:196px;top:232px;width:392px;height:220px;background:var(--white);padding:34px 30px}
.hero-card h1{font-size:21px;font-weight:900;color:var(--navy);line-height:1.35;text-transform:uppercase}
.hero-card h1 em{font-style:normal;color:var(--blue)}
.hero-card p{font-size:11.5px;margin-top:12px}
.btn-outline{display:inline-block;margin-top:20px;border:1.5px solid var(--green);color:var(--green);font-size:10.5px;font-weight:900;text-transform:uppercase;padding:6px 18px;text-decoration:none}

/* intro */
.section-title{font-size:24px;font-weight:700;color:var(--navy);display:flex;align-items:center;gap:14px}
.section-title::before{content:"";width:9px;height:9px;background:var(--green);display:block}
.intro-title{left:160px;top:618px}
.intro-photo{left:160px;top:678px;width:489px;height:197px;background:linear-gradient(180deg,#7fb2e4 0%,#cfe2f2 45%,#c8b59c 70%,#8a7d6b 100%)}
.sub-title{font-size:16px;font-weight:900;color:var(--navy);text-transform:uppercase;display:flex;align-items:center;gap:10px}
.sub-title::before{content:"";width:7px;height:7px;background:var(--green);display:block}
.about{left:160px;top:890px;width:489px}
.about p{margin-top:10px;font-size:11.5px}
.appt-title{left:703px;top:676px}
.appt-form{left:703px;top:719px;width:337px;height:327px;background:var(--blue);padding:14px 14px;display:grid;grid-template-columns:1fr 1fr;column-gap:14px;row-gap:6px;align-content:start}
.field label{display:block;color:var(--white);font-size:9.5px;line-height:1.4}
.field span{display:block;height:24px;background:var(--white)}
.field.wide{grid-column:1/3}
.field.area span{height:54px}
.send{grid-column:1/3;height:28px;background:var(--navy);color:var(--white);font-size:10.5px;font-weight:900;text-align:center;line-height:28px;text-transform:uppercase;margin-top:6px}

/* services */
.services{left:0;top:1107px;width:1200px;height:505px;background:var(--green)}
.centered-title{position:absolute;left:0;width:1200px;text-align:center;font-size:26px;font-weight:900;text-transform:uppercase;color:var(--navy)}
.centered-title::before,.centered-title::after{content:"";display:inline-block;width:8px;height:8px;background:currentColor;vertical-align:middle;margin:0 16px 4px}
.services .centered-title{color:var(--white);top:40px}
.svc-card{top:107px;width:277px;height:346px;background:var(--white);padding:14px;box-shadow:0 10px 18px rgba(0,0,0,.25)}
.svc-img{height:150px}
.svc-card h3{font-size:15px;font-weight:900;color:var(--navy);text-transform:uppercase;margin-top:14px}
.svc-card p{font-size:11.5px;margin-top:4px}
.more{display:block;font-size:10.5px;font-weight:900;color:var(--navy);text-transform:uppercase;margin-top:14px}
.slider-arrow{top:265px;width:38px;height:38px;border-radius:50%;border:1.5px solid rgba(255,255,255,.8);display:flex;align-items:center;justify-content:center}
.slider-arrow.solid{background:var(--white)}

/* why */
.why-title{top:1650px;color:var(--navy)}
.why-title::before,.why-title::after{background:var(--green)}
.perk{top:1724px;width:150px;text-align:center}
.perk svg{display:block;margin:0 auto}
.perk h4{font-size:11.5px;font-weight:700;color:var(--navy);line-height:1.35;margin-top:10px}

/* finance band */
.finance{left:0;top:1890px;width:1200px;height:113px;background:var(--blue)}
.finance p{position:absolute;left:160px;top:32px;color:var(--white);font-size:15px;font-weight:700;line-height:1.5}
.btn-white{position:absolute;left:836px;top:42px;width:204px;height:30px;background:var(--white);color:var(--navy);font-size:10.5px;font-weight:900;text-transform:uppercase;text-align:center;line-height:30px}

/* media */
.media-col{top:2050px;width:270px}
.media-head{display:flex;align-items:center;justify-content:space-between;height:50px}
.media-head h2{font-size:26px;font-weight:900;color:var(--navy);text-transform:uppercase;display:flex;align-items:center;gap:14px}
.media-head h2::after{content:"";width:8px;height:8px;background:var(--green);display:block}
.media-img{height:150px;margin-top:20px}
.media-col h3{font-size:16px;font-weight:700;color:var(--navy);line-height:1.4;margin-top:14px}
.media-col p{font-size:11.5px;margin-top:8px}
.date{font-size:10.5px;color:var(--green);margin-top:6px}
.view-all{position:absolute;top:393px;font-size:10.5px;font-weight:900;color:var(--navy);text-transform:uppercase}
.gallery-grid{display:grid;grid-template-columns:1fr 1fr;gap:8px;margin-top:20px;width:205px}
.gallery-grid .wide{grid-column:1/3;height:150px}
.gallery-grid .half{height:127px}

/* testimonials */
.testimonials{left:0;top:2513px;width:1200px;height:448px;background:linear-gradient(180deg,#0c1322 0%,#16233a 60%,#0b1220 100%)}
.testimonials .centered-title{color:var(--white);top:44px}
.quote-card{left:312px;top:143px;width:576px;height:244px;background:var(--white);text-align:center;padding:80px 56px 0}
.quote-card p{font-size:11.5px;font-style:italic}
.quote-card h4{font-size:12px;color:var(--green);font-style:italic;margin-top:8px}
.quote-card small{font-size:11px;font-style:italic}
.avatar{left:570px;top:95px;width:60px;height:60px;border-radius:50%;background:#c8ccd2;border:4px solid var(--white)}
.t-arrow{top:255px;color:#9aa3b2;font-size:26px}
.dots{left:568px;top:2901px;display:flex;gap:6px}
.dots span{width:14px;height:3px;background:#56627a}
.dots span.on{background:var(--blue)}

/* footer */
.footer-bar{left:0;top:2961px;width:1200px;height:74px;background:var(--light)}
.footer-call{left:160px;top:2975px;color:var(--navy)}
.footer-call small{display:block;font-size:11.5px;font-weight:900;text-transform:uppercase}
.footer-call strong{display:block;color:var(--green);font-size:23px;font-weight:900;line-height:1.2}
.connect{left:456px;top:2975px}
.connect small{display:block;font-size:11.5px;font-weight:900;color:var(--navy);text-transform:uppercase}
.connect div{display:flex;gap:8px;margin-top:8px}
.connect span{width:22px;height:22px;border-radius:50%;background:#d9dde1;display:block}
.connect span:first-child{background:var(--green)}
.subscribe{left:764px;top:2961px;width:276px;height:185px;background:var(--green);padding:20px 16px;clip-path:polygon(0 0,100% 0,100% 82%,50% 100%,0 82%)}
.subscribe h3{color:var(--white);font-size:16px;font-weight:900;text-transform:uppercase}
.subscribe p{color:var(--white);font-size:10.5px;line-height:1.45;margin-top:2px}
.sub-input{margin-top:14px;height:28px;background:var(--white);border-radius:14px;display:flex;align-items:center;justify-content:space-between;padding:0 4px 0 12px;font-size:9.5px;color:#888}
.sub-input b{background:var(--navy);color:var(--white);border-radius:11px;padding:3px 12px;font-size:9.5px}
.footer-brand{left:160px;top:3100px;display:flex;align-items:center;gap:10px}
.contact-line{left:160px;display:flex;gap:10px;font-size:10.5px;line-height:1.4;color:var(--text)}
.footer-links{width:200px}
.footer-links h3{font-size:15px;font-weight:900;color:var(--navy);text-transform:uppercase;display:flex;align-items:center;gap:9px}
.footer-links h3::before{content:"";width:7px;height:7px;background:var(--green);display:block}
.footer-links ul{list-style:none;margin-top:10px}
.footer-links li{font-size:10.5px;line-height:21px;color:var(--text)}
.footer-links li.active{color:var(--green)}
.pay{left:764px;top:3170px}
.pay p{font-size:10.5px;line-height:1.4;width:260px}
.pay div{display:flex;gap:6px;margin-top:10px}
.pay span{width:52px;height:34px;border-radius:3px;display:block;border:1px solid #d6d9dd}
.copy{left:0;top:3341px;width:1200px;height:49px;border-top:1px solid #e3e6e8;padding:14px 160px;font-size:10.5px}
</style>
</head>
<body>

<header class="site-header">
  <div class="abs brand"><span class="brand-dot"></span><span class="brand-name">Marlowe Oakhaven Builders LLC</span></div>
  <div class="abs social" aria-label="Social links"><span></span><span></span><span></span><span></span></div>
  <div class="abs call"><small>CALL TODAY FOR A FREE ESTIMATE!</small><strong>1-877-555-0148</strong></div>
  <nav class="abs main-nav">
    <a class="active">Home</a><a>Roofing</a><a>Siding &amp; Gutters</a><a>Windows</a><a>Discounts</a><a>Financing</a><a>Resources</a><a>Contact</a>
  </nav>
</header>

<section class="abs hero" role="img" aria-label="Worker in a blue cap installing a metal gutter along a roof edge under blue sky"></section>
<div class="abs hero-card">
  <h1>Master <em>Roofing</em>, <em>Windows</em> &amp;<br><em>Gutters</em> Experts.</h1>
  <p>Lorem ipsum dolor sit amet, consectetur adipiscing elit, sed do eiusmod tempor incididunt ut labore et dolore magna aliqua.</p>
  <a class="btn-outline">View Services &rarr;</a>
</div>

<h2 class="abs section-title intro-title">Roofing, Gutters, and Windows Company —Services &amp; Repair</h2>
<div class="photo intro-photo" role="img" aria-label="Two-storey stone and stucco house with red tile roof"></div>
<div class="abs about">
  <h3 class="sub-title">About Us</h3>
  <p>Lorem ipsum dolor sit amet, consectetur adipiscing elit, sed do eiusmod tempor incididunt ut labore et dolore magna aliqua. Ut enim ad minim veniam, quis nostrud exercitation ullamco laboris nisi ut aliquip ex ea commodo consequat. Duis aute irure dolor in reprehenderit in voluptate velit esse cillum dolore eu fugiat nulla pariatur.</p>
  <p>Sed ut perspiciatis unde omnis iste natus error sit voluptatem accusantium doloremque laudantium, totam rem aperiam, eaque ipsa quae ab illo inventore.</p>
</div>
<h3 class="abs sub-title appt-title">Schedule an Appointment</h3>
<form class="abs appt-form" aria-label="Schedule an appointment">
  <div class="field"><label>First Name</label><span></span></div>
  <div class="field"><label>Last Name</label><span></span></div>
  <div class="field"><label>Email</label><span></span></div>
  <div class="field"><label>Phone</label><span></span></div>
  <div class="field wide"><label>Address</label><span></span></div>
  <div class="field"><label>City</label><span></span></div>
  <div class="field"><label>State</label><span></span></div>
  <div class="field wide area"><label>How can we help you?</label><span></span></div>
  <div class="send">Send</div>
</form>

<section class="abs services">
  <h2 class="centered-title">Our Home Improvement Services</h2>
  <div class="abs slider-arrow" style="left:90px"><svg width="12" height="12" viewBox="0 0 12 12"><path d="M8 1 3 6l5 5" stroke="#fff" stroke-width="1.6" fill="none"/></svg></div>
  <article class="abs svc-card" style="left:160px">
    <div class="svc-img" role="img" aria-label="Roofers working on a red tiled roof" style="background:linear-gradient(180deg,#9cc3e6,#8b3b2c)"></div>
    <h3>Roofing</h3>
    <p>Lorem ipsum dolor sit amet, consectetur adipiscing elit, sed do eiusmod tempor incididunt ut labore et dolore magna aliqua. Ut enim ad minim veniam, quis</p>
    <span class="more">Read More &rsaquo;</span>
  </article>
  <article class="abs svc-card" style="left:461px">
    <div class="svc-img" role="img" aria-label="Two installers fitting a large window" style="background:linear-gradient(180deg,#eef1f3,#b9c2c4)"></div>
    <h3>Windows</h3>
    <p>Lorem ipsum dolor sit amet, consectetur adipiscing elit, sed do eiusmod tempor incididunt ut labore et dolore magna aliqua. Ut enim ad minim veniam, quis</p>
    <span class="more">Read More &rsaquo;</span>
  </article>
  <article class="abs svc-card" style="left:763px">
    <div class="svc-img" role="img" aria-label="Worker fixing a downspout gutter on a wall" style="background:linear-gradient(180deg,#a9cdea,#6f7c85)"></div>
    <h3>Gutters</h3>
    <p>Lorem ipsum dolor sit amet, consectetur adipiscing elit, sed do eiusmod tempor incididunt ut labore et dolore magna aliqua. Ut enim ad minim veniam, quis</p>
    <span class="more">Read More &rsaquo;</span>
  </article>
  <div class="abs slider-arrow solid" style="left:1072px"><svg width="12" height="12" viewBox="0 0 12 12"><path d="M4 1l5 5-5 5" stroke="#078a3d" stroke-width="1.6" fill="none"/></svg></div>
</section>

<h2 class="centered-title why-title">Why Hire Us?</h2>
<div class="abs perk" style="left:153px"><svg width="44" height="44" viewBox="0 0 44 44" fill="none" stroke="#078a3d" stroke-width="2"><circle cx="22" cy="22" r="18"/><circle cx="22" cy="22" r="12"/><path d="M16 22l4 4 8-8"/></svg><h4>100% Satisfaction<br>Guarantee</h4></div>
<div class="abs perk" style="left:302px"><svg width="44" height="44" viewBox="0 0 44 44" fill="none" stroke="#078a3d" stroke-width="2"><circle cx="22" cy="22" r="18"/><path d="M9 9l26 26M26 15h-6a3 3 0 0 0 0 6h4a3 3 0 0 1 0 6h-6M22 12v20"/></svg><h4>No Surprises or<br>Hidden Costs.</h4></div>
<div class="abs perk" style="left:452px"><svg width="44" height="44" viewBox="0 0 44 44" fill="none" stroke="#078a3d" stroke-width="2"><rect x="8" y="6" width="26" height="32" rx="2"/><path d="M13 13h16M13 20h6M23 20h6M13 27h6M23 27h6"/></svg><h4>0% Interest<br>Free Financing</h4></div>
<div class="abs perk" style="left:598px"><svg width="44" height="44" viewBox="0 0 44 44" fill="none" stroke="#078a3d" stroke-width="2"><path d="M12 18a10 10 0 0 1 20 0zM10 18h24M16 22a6 6 0 0 0 12 0M8 40c2-8 8-10 14-10s12 2 14 10"/></svg><h4>Highly Trained<br>Employees</h4></div>
<div class="abs perk" style="left:745px"><svg width="44" height="44" viewBox="0 0 44 44" fill="none" stroke="#078a3d" stroke-width="2"><circle cx="22" cy="18" r="12"/><path d="M17 18l4 4 7-7M15 28l-4 12 6-3 3 5 2-12M29 28l4 12-6-3-3 5"/></svg><h4>Offering 30-50 Year<br>Warranties</h4></div>
<div class="abs perk" style="left:890px"><svg width="44" height="44" viewBox="0 0 44 44" fill="none" stroke="#078a3d" stroke-width="2"><path d="M10 8l6 0 3 8-4 3a18 18 0 0 0 10 10l3-4 8 3v6a3 3 0 0 1-3 3C20 37 7 24 7 11a3 3 0 0 1 3-3z"/><rect x="24" y="4" width="14" height="14" rx="2"/><path d="M31 7v8M27 11h8"/></svg><h4>Emergency Services<br>Available</h4></div>

<section class="abs finance">
  <p>Do you need new roofing, gutters or windows? We offer 0% 6 months interest<br>free financing with approved credit.</p>
  <span class="btn-white">Schedule an Appointment &rarr;</span>
</section>

<div class="abs media-col" style="left:160px">
  <div class="media-head"><h2>Gallery</h2><svg width="40" height="34" viewBox="0 0 40 34" fill="none" stroke="#078a3d" stroke-width="2"><rect x="2" y="6" width="30" height="24"/><path d="M8 2h30v22M5 26l9-9 6 6 5-4 7 7"/></svg></div>
  <div class="gallery-grid">
    <div class="wide" role="img" aria-label="Installers fitting a window frame" style="background:linear-gradient(180deg,#eef0f1,#b8bcbf)"></div>
    <div class="half" role="img" aria-label="Worker repairing a gutter" style="background:linear-gradient(180deg,#cfe0ee,#8a8f93)"></div>
    <div class="half" role="img" aria-label="Roofer laying red tiles" style="background:linear-gradient(180deg,#c2c8cc,#a1422f)"></div>
  </div>
  <span class="view-all">View All Photos &#9638;</span>
</div>

<div class="abs media-col" style="left:466px">
  <div class="media-head"><h2>Videos</h2><svg width="40" height="34" viewBox="0 0 40 34" fill="none" stroke="#078a3d" stroke-width="2"><rect x="2" y="2" width="36" height="30"/><path d="M2 9h36M9 2v7M16 2v7M23 2v7M30 2v7M16 15l9 5-9 5z"/></svg></div>
  <div class="media-img" role="img" aria-label="Video still of roofers working on a tiled roof at dusk" style="background:linear-gradient(180deg,#3b4658,#7b5a48)"></div>
  <h3>Sed ut perspiciatis unde omnis iste natus error sit voluptatem</h3>
  <p>Lorem ipsum dolor sit amet, consectetur adipiscing elit, sed do eiusmod tempor incididunt ut labore et dolore magna aliqua. Ut enim ad minim veniam, quis nostrud exercitation ullamco laboris.</p>
  <span class="view-all">View All Videos &#9638;</span>
</div>

<div class="abs media-col" style="left:770px">
  <div class="media-head"><h2>Events</h2><svg width="40" height="34" viewBox="0 0 40 34" fill="none" stroke="#078a3d" stroke-width="2"><rect x="4" y="4" width="32" height="28" rx="2"/><path d="M4 12h32M12 1v6M28 1v6M11 18h4M18 18h4M25 18h4M11 25h4M18 25h4"/></svg></div>
  <div class="media-img" role="img" aria-label="Red metal roof on a building" style="height:106px;background:linear-gradient(180deg,#c9342a,#8e2019)"></div>
  <h3>Sed ut perspiciatis unde omnis</h3>
  <div class="date">&#9638; 29 May 2019</div>
  <p>Lorem ipsum dolor sit amet, consectetur adipiscing elit, sed do eiusmod tempor incididunt ut labore et dolore magna aliqua. Ut enim ad minim veniam, quis nostrud exercitation ullamco laboris nisi ut aliquip ex ea commodo consequat. Duis aute irure dolor in reprehenderit in voluptate velit esse.</p>
  <span class="view-all">View All Events &#9638;</span>
</div>

<section class="abs testimonials">
  <h2 class="centered-title">Testimonials</h2>
  <span class="abs t-arrow" style="left:232px">&lsaquo;</span>
  <div class="abs quote-card">
    <p>Lorem ipsum dolor sit amet, consectetur adipiscing elit, sed do eiusmod tempor incididunt ut labore et dolore magna aliqua. Ut enim ad minim veniam, quis nostrud exercitation ullamco laboris nisi ut aliquip ex ea commodo consequat.</p>
    <h4>User Name</h4>
    <small>Lorem ipsum dolor</small>
  </div>
  <div class="abs avatar"></div>
  <span class="abs t-arrow" style="left:956px">&rsaquo;</span>
</section>
<div class="abs dots"><span class="on"></span><span></span><span></span></div>

<footer>
  <div class="abs footer-bar"></div>
  <div class="abs footer-call"><small>Call Today for a Free Estimate!</small><strong>1-877-555-0148</strong></div>
  <div class="abs connect"><small>Connect With Us</small><div><span></span><span></span><span></span><span></span></div></div>
  <div class="abs subscribe">
    <h3>Subscribe Us</h3>
    <p>Subscribe to our newsletter to get latest news and offer updates</p>
    <div class="sub-input">Enter your email address <b>Send</b></div>
  </div>

  <div class="abs footer-brand"><span class="brand-dot"></span><span class="brand-name">Marlowe Oakhaven Builders LLC</span></div>
  <div class="abs contact-line" style="top:3205px"><svg width="12" height="16" viewBox="0 0 12 16" fill="none" stroke="#555c66" stroke-width="1.4"><path d="M6 15S1 9 1 6a5 5 0 0 1 10 0c0 3-5 9-5 9z"/><circle cx="6" cy="6" r="2"/></svg><span>48 Harrow Lane, Elm Ridge,<br>AB 010203</span></div>
  <div class="abs contact-line" style="top:3243px"><svg width="14" height="12" viewBox="0 0 14 12" fill="none" stroke="#555c66" stroke-width="1.4"><rect x="1" y="1" width="12" height="10"/><path d="M1 1l6 5 6-5"/></svg><span>info@oakhavenbuild.com</span></div>

  <div class="abs footer-links" style="left:389px;top:3080px">
    <h3>Quick Links</h3>
    <ul><li class="active">Home</li><li>Roofing</li><li>Siding &amp; Gutters</li><li>Windows</li><li>Discounts</li><li>Financing</li><li>Resources</li><li>Contact</li></ul>
  </div>
  <div class="abs footer-links" style="left:588px;top:3080px">
    <h3>Our Services</h3>
    <ul><li>Roofing</li><li>Windows</li><li>Gutters</li><li>Quorvin Windows</li><li>Tillbrook Windows</li><li>RUV Roofing Shingles</li><li>PEM Roofing Shingles</li><li>Emergency Services</li></ul>
  </div>
  <div class="abs pay">
    <p>Accepting all major Credit Cards and Checks</p>
    <div aria-label="Accepted payment cards"><span style="background:#1d2f5e"></span><span style="background:#f3f4f6"></span><span style="background:#2a7bc0"></span><span style="background:#f3f4f6"></span></div>
  </div>
  <div class="abs copy">Copyright &copy; 2019 Marlowe Oakhaven | All Rights Reserved</div>
</footer>

</body>
</html>
```